Hawaii Real Estate Resort Report; Direct mail design template

Aloha designers!
Full color Bi-fold design template for a monthly or quarterly Hawaii real estate publication titled "The Coastline Ledger". Design needs to be visually appealing and able to utilize various photos, text sections, graphs or charts, etc. For the Pali Kemu Resort area on the southwest side of Oahu.
Needs to have a blank/clear area on the outside for mailing purposes and to adhere with NMDA requirements. (http://docs.nmda-example.org/fsm/documents/tech_guides/FSMReference.pdf)
Final design needs to be in an Adobe Illustrator (.ai) format per the attached PressLoom.com templates. Bleed areas provided in the templates need to be adhered to so that we have a print-ready template with the necessary bleed areas.
All text areas need to be able to be edited and should not have outlined fonts unless it is text that will never be changed (ie: the title "The Coastline Ledger"). Final design should incorporate appealing fonts and colors so that various text can be entered in and text size adjusted as needed.
The design template should incorporate a similar look and feel (color scheme) as the attached two-sided marketing info flyer on our vacation rental management services.
We can provide images, logos and other design components as needed.
Content helps:
- The Coastline Ledger
- Specializing in Resort Real Estate & Vacation Rentals
- Volume 1, Issue 1
- Sections: Main body message section for welcome note/letter, sort of like an Editor's note. Resort Real Estate Sales From DATE to DATE (list or chart), Shore Cottages at Pali Kemu Sales Update, Text areas for updates on some of the six resort communities, Photo of the month, Local Business Spotlight, Fun Facts section in sidebar (small area). Contact information with photo, name, phone, email, website.
Mahalo!
Updates
Just let me know if there are specific images or other content details that you require to create an initial design template. Thanks.

```html
<!DOCTYPE html>
<html lang="en">
<head>
<meta charset="utf-8">
<title>The Coastline Ledger – Market Update Mailer</title>
<link href="https://fonts.googleapis.com/css2?family=Barlow:wght@600;700&family=PT+Sans:wght@400;700&display=swap" rel="stylesheet">
<style>
  :root {
    --gold: #c9ad62;
    --red: #ae1f2f;
    --red-deep: #9b1a28;
    --ink: #2a2526;
    --charcoal: #231f20;
    --paper: #ffffff;
    --backdrop: #e8e4dd;
    --rule: #8a8a8a;
    --cream: #f3e6c4;
  }
  * { box-sizing: border-box; margin: 0; padding: 0; }
  html, body { width: 1200px; height: 900px; overflow: hidden; }
  body { background: var(--backdrop); font-family: "PT Sans", Arial, sans-serif; color: var(--ink); }

  .mailer {
    position: absolute; left: 260px; top: 20px; width: 680px; height: 860px;
    background: var(--paper); box-shadow: 0 4px 18px rgba(0,0,0,.18); overflow: hidden;
  }

  /* Left: market update + mailing panel */
  .market { position: absolute; left: 0; top: 0; width: 438px; height: 860px; }
  .market-header { background: var(--gold); height: 72px; padding: 8px 16px 0; }
  .market-title { font-family: "Barlow", Arial, sans-serif; font-weight: 700; color: var(--red); font-size: 37px; line-height: 1; }
  .market-subtitle { font-family: "Barlow", Arial, sans-serif; font-weight: 600; color: var(--red); font-size: 20px; line-height: 1.2; }

  .market-body { display: flex; gap: 16px; padding: 10px 16px 0; height: 250px; overflow: hidden; }
  .market-col { flex: 1; font-size: 9.5px; line-height: 12.4px; text-align: justify; }
  .market-col p { margin-bottom: 8px; }
  .market-col h3 { color: var(--red); font-size: 11.5px; font-weight: 700; margin: 4px 0 2px; line-height: 1.2; }

  .contact-bar { background: var(--charcoal); height: 62px; padding: 5px 12px; color: #fff; position: relative; }
  .contact-lead { font-size: 7.5px; font-weight: 700; margin-left: 52px; }
  .agent-photo { position: absolute; left: 12px; top: 7px; width: 44px; height: 48px; background: linear-gradient(#b79e84, #6e5a4c); border: 2px solid var(--red); }
  .agent-name { position: absolute; left: 66px; top: 20px; font-family: "Barlow", Arial, sans-serif; font-weight: 700; color: var(--gold); font-size: 13px; }
  .agent-role { position: absolute; left: 66px; top: 36px; font-size: 8px; color: #ddd; font-style: normal; }
  .agent-lines { position: absolute; left: 190px; top: 17px; font-size: 7px; line-height: 9px; color: #eee; list-style: none; }
  .agent-license { position: absolute; left: 190px; bottom: 2px; font-size: 5.5px; color: #999; }
  .brokerage { position: absolute; right: 12px; top: 26px; display: flex; align-items: center; gap: 5px; font-family: "PT Sans", Arial, sans-serif; font-weight: 700; font-size: 11px; color: #fff; }
  .brokerage-square { width: 10px; height: 10px; background: #fff; }

  .mail-panel { position: relative; height: 476px; }
  .address-lines { position: absolute; left: 142px; top: 122px; width: 222px; }
  .address-lines span { display: block; height: 1px; background: var(--rule); margin-bottom: 29px; }
  .stamp-box { position: absolute; left: 28px; top: 326px; width: 78px; height: 82px; border: 1.5px solid var(--ink); }

  /* Right sidebar */
  .sidebar { position: absolute; left: 444px; top: 0; width: 236px; height: 860px; }
  .photo-month { background: var(--red); height: 216px; padding: 8px 9px; color: #fff; }
  .sidebar-title { font-family: "Barlow", Arial, sans-serif; font-weight: 700; font-size: 19px; line-height: 1.1; }
  .photo-month .sidebar-title { color: var(--cream); margin-bottom: 6px; }
  .photo-month-image { height: 132px; background: linear-gradient(#8fc4e8 0%, #57a3c9 45%, #2f7d6a 70%, #1f5b47 100%); border: 2px solid #fff; }
  .photo-month-caption { font-size: 7px; line-height: 8.5px; margin-top: 5px; }

  .spotlight { margin-top: 8px; height: 172px; }
  .spotlight .sidebar-title { background: var(--gold); color: var(--red); padding: 6px 9px; }
  .spotlight-body { padding: 7px 9px; font-size: 7.5px; line-height: 9.6px; text-align: justify; }
  .spotlight-image { float: right; width: 78px; height: 66px; margin: 0 0 4px 6px; background: linear-gradient(135deg, #d6c3a0, #7b6247); }

  .brand-panel { position: absolute; top: 398px; left: 0; width: 236px; height: 462px; background: var(--red); color: #fff; }
  .brand-circle { position: absolute; left: 78px; top: 36px; width: 80px; height: 80px; border-radius: 50%; background: var(--cream); }
  .brand-back { position: absolute; left: 0; top: 150px; width: 236px; height: 300px; transform: rotate(180deg); text-align: center; padding-top: 12px; }
  .brand-back-copy { font-size: 7px; line-height: 8.8px; padding: 0 14px; text-align: left; }
  .brand-name { margin-top: 150px; font-family: "PT Sans", Arial, sans-serif; font-weight: 700; font-size: 24px; color: #fff; }
  .brand-tagline { font-size: 7.5px; color: #fff; margin-top: 2px; }
</style>
</head>
<body>
<main class="mailer">
  <section class="market">
    <header class="market-header">
      <h1 class="market-title">How’s The Market?</h1>
      <p class="market-subtitle">Market updates, info</p>
    </header>
    <div class="market-body">
      <div class="market-col">
        <p>Lorem ipsum dolor sit amet, consectetur adipisicing elit, sed do eiusmod tempor incididunt ut labore et dolore magna aliqua. Ut enim ad minim veniam, quis nostrud exercitation ullamco laboris nisi ut aliquip ex ea commodo consequat.</p>
        <h3>consectetur adipisicing</h3>
        <p>Sed ut perspiciatis unde omnis iste natus error sit voluptatem accusantium doloremque laudantium, totam rem aperiam, eaque ipsa quae ab illo inventore veritatis et quasi architecto beatae vitae dicta sunt explicabo.</p>
        <p>Nemo enim ipsam voluptatem quia voluptas sit aspernatur aut odit aut fugit, sed quia consequuntur magni dolores eos qui ratione voluptatem sequi nesciunt.</p>
      </div>
      <div class="market-col">
        <p>Neque porro quisquam est, qui dolorem ipsum quia dolor sit amet, consectetur, adipisci velit, sed quia non numquam eius modi tempora incidunt ut labore et dolore magnam aliquam quaerat voluptatem.</p>
        <h3>consectetur adipisicing</h3>
        <p>Ut enim ad minima veniam, quis nostrum exercitationem ullam corporis suscipit laboriosam, nisi ut aliquid ex ea commodi consequatur? Quis autem vel eum iure reprehenderit qui in ea voluptate velit.</p>
        <p>Ut enim ad minima veniam, quis nostrum exercitationem ullam corporis suscipit laboriosam, nisi ut aliquid ex ea commodi consequatur? Quis autem vel eum iure reprehenderit.</p>
      </div>
    </div>
    <div class="contact-bar">
      <p class="contact-lead">Contact Dane Halverson for a FREE no obligation assessment of the villa you own or intend to purchase.</p>
      <div class="agent-photo" role="img" aria-label="Agent portrait photo"></div>
      <p class="agent-name">Dane Halverson</p>
      <p class="agent-role">RA, MBA, Property Manager</p>
      <ul class="agent-lines">
        <li>Cell: 808.555.0142</li>
        <li>Office: 808.555.0187</li>
        <li>Email: dane@makaistays-example.com</li>
        <li>www.danehalverson-example.com</li>
      </ul>
      <p class="agent-license">License RB-00000</p>
      <div class="brokerage"><span class="brokerage-square"></span>Harborline Homes</div>
    </div>
    <div class="mail-panel">
      <div class="address-lines"><span></span><span></span><span></span><span></span><span></span></div>
      <div class="stamp-box"></div>
    </div>
  </section>

  <aside class="sidebar">
    <section class="photo-month">
      <h2 class="sidebar-title">Photo of the Month</h2>
      <div class="photo-month-image" role="img" aria-label="Resort pool and palm trees by the ocean"></div>
      <p class="photo-month-caption">Lorem ipsum dolor sit amet, consectetur adipisicing elit, sed do eiusmod tempor incididunt ut labore et dolore magna aliqua. Ut enim ad minim veniam, quis nostrud exercitation ullamco laboris nisi.</p>
    </section>
    <section class="spotlight">
      <h2 class="sidebar-title">Business Spotlight</h2>
      <div class="spotlight-body">
        <div class="spotlight-image" role="img" aria-label="Local business photo"></div>
        Lorem ipsum dolor sit amet, consectetur adipisicing elit, sed do eiusmod tempor incididunt ut labore et dolore magna aliqua. Ut enim ad minim veniam, quis nostrud exercitation ullamco laboris nisi ut aliquip ex ea commodo consequat. Duis aute irure dolor in reprehenderit in voluptate velit esse cillum dolore eu fugiat nulla pariatur.
      </div>
    </section>
    <section class="brand-panel">
      <div class="brand-circle"></div>
      <div class="brand-back">
        <p class="brand-back-copy">Lorem ipsum dolor sit amet, consectetur adipisicing elit, sed do eiusmod tempor incididunt ut labore et dolore magna aliqua. Ut enim ad minim veniam, quis nostrud exercitation ullamco laboris nisi ut aliquip ex ea commodo consequat.</p>
        <p class="brand-name">Makai Stays</p>
        <p class="brand-tagline">Pali Kemu Vacation Rental Management</p>
      </div>
    </section>
  </aside>
</main>
</body>
</html>
```